LOGO DESIGN: Construction Related Service Business

We require a logo for our business Dovtar Services. We are a construction related business offering a range of services including machine services for groundworks (digging trenches, soak wells, preparing land for construction etc), demolition and truck haulage from demolition sites.
We would like our logo to be predominately text, but may include abstract graphics. The colour scheme should be mainly a mid bright blue and overall be quite 'clean'.

Industry/Entity Type

Construction

Contact Information for Business Card

Colin Pruett
Ph:041 562 9083
dovtarservices@keloran.com.au

Colors
0456a3

```html
<!DOCTYPE html>
<html lang="en">
<head>
<meta charset="UTF-8">
<title>Dovtar Services – Business Card</title>
<link rel="stylesheet" href="https://fonts.googleapis.com/css2?family=Questrial&display=swap">
<style>
  :root {
    --page-bg: #ffffff;
    --card-white: #ffffff;
    --card-white-shade: #eeeeef;
    --brand-blue: #0456a3;
    --band-blue: #3a5fc4;
    --name-blue: #3f5fbd;
    --tagline-ink: #151a24;
    --panel-top: #1b1c1f;
    --panel-bottom: #050506;
    --contact-ink: #ffffff;
    --icon-blue: #4a6fd0;
  }

  * { margin: 0; padding: 0; box-sizing: border-box; }

  html, body {
    width: 1200px;
    height: 900px;
    overflow: hidden;
    background: var(--page-bg);
    font-family: "Questrial", "Century Gothic", sans-serif;
  }

  .canvas {
    position: relative;
    width: 1200px;
    height: 900px;
  }

  .business-card {
    position: absolute;
    left: 160px;
    top: 195px;
    width: 880px;
    height: 510px;
    border-radius: 42px;
    overflow: hidden;
    box-shadow: 0 18px 40px rgba(0, 0, 0, 0.18);
    display: flex;
    flex-direction: column;
  }

  .card-header {
    height: 255px;
    background: linear-gradient(to bottom, var(--card-white) 0%, var(--card-white) 45%, var(--card-white-shade) 100%);
    display: flex;
    align-items: center;
    justify-content: center;
    padding-top: 30px;
  }

  .brand-name {
    color: var(--brand-blue);
    font-size: 78px;
    font-weight: 400;
    letter-spacing: 2px;
    line-height: 1;
  }

  .tagline-band {
    height: 28px;
    background: var(--band-blue);
    display: flex;
    align-items: center;
    justify-content: center;
  }

  .tagline {
    color: var(--tagline-ink);
    font-size: 17px;
    letter-spacing: 6px;
    text-transform: uppercase;
    white-space: nowrap;
  }

  .card-body {
    flex: 1;
    background: linear-gradient(to bottom, var(--panel-top), var(--panel-bottom));
    padding: 82px 0 0 70px;
  }

  .contact-name {
    color: var(--name-blue);
    font-size: 34px;
    margin-bottom: 52px;
  }

  .contact-list {
    list-style: none;
  }

  .contact-item {
    display: flex;
    align-items: center;
    gap: 14px;
    color: var(--contact-ink);
    font-size: 27px;
    line-height: 1.3;
  }

  .contact-icon {
    width: 30px;
    height: 26px;
    flex: none;
  }
</style>
</head>
<body>
<main class="canvas">
  <article class="business-card">
    <header class="card-header">
      <h1 class="brand-name">Dovtar Services</h1>
    </header>

    <div class="tagline-band">
      <p class="tagline">Whatever it takes...we make it happen</p>
    </div>

    <section class="card-body">
      <h2 class="contact-name">Colin Pruett</h2>
      <ul class="contact-list">
        <li class="contact-item">
          <svg class="contact-icon" viewBox="0 0 30 26" aria-hidden="true">
            <path fill="var(--icon-blue)" d="M7 2c1.2-.6 2.2 0 2.8 1l2.4 4c.6 1 .3 2-.5 2.6l-1.6 1.2c1.2 2.6 3.4 5 6 6.4l1.3-1.5c.7-.8 1.8-1 2.7-.4l3.8 2.6c1 .7 1.2 1.8.5 2.8l-1.6 2.2c-.9 1.2-2.4 1.6-3.8 1.1C11.3 21.3 5.2 14.7 3.3 7.3 3 5.9 3.5 4.5 4.7 3.6z"/>
          </svg>
          <span>041 562 9083</span>
        </li>
        <li class="contact-item">
          <svg class="contact-icon" viewBox="0 0 30 26" aria-hidden="true">
            <rect x="2" y="6" width="26" height="17" fill="var(--icon-blue)"/>
            <path d="M2 6l13 10L28 6" fill="none" stroke="#ffffff" stroke-width="1.6"/>
            <path d="M2 23l10-8M28 23l-10-8" fill="none" stroke="#ffffff" stroke-width="1.2"/>
          </svg>
          <span>dovtarservices@keloran.com.au</span>
        </li>
      </ul>
    </section>
  </article>
</main>
</body>
</html>
```